Banners for website home page

I'm looking for 3 banners that will rotate on my website carousel addressing my 3 target markets. The website is Ledgerwise Harbor.

1) Young Starters
Headline: Start smart. Invest with confidence.
Sub: Learn the basics, set your first goal, and build a long-term plan with Ledgerwise Harbor.
CTA: Start free
Hero image ideas: Young person with phone/laptop; app UI overlay; subtle navy/gold chart shapes.

2) Saving for a Goal
Headline: Turn your goal into a plan.
Sub: Home deposit or child’s education—set targets, see projections, and track progress.
CTA: Plan my goal
Hero image ideas: Couple/family looking at house plans or a uni cap; progress bar overlay; warm light.

3) Retirement Fund Owners
Headline: Grow and protect your Retirement Fund.
Sub: Professional-grade tracking and signals to help your super grow—and last.
CTA: Start Now
Hero image ideas: Mature couple with tablet / beach walk; portfolio charts/compass motif overlaid.

Our app does the following:
Ledgerwise Harbor is an easy-to-use app designed to help everyday people take control of their investing journey.
Backed by over 10 years of proven investment models and experience, it empowers you to set realistic goals, build a tailored investment plan, and confidently manage your risk. With built-in education, alerts, and market insights, Ledgerwise Harbor helps you stay on course and maximise returns—no guesswork, just smart investing.

See attached an example AI generated banner and current logo to base colours, feel. for the website I use a dark blue menu and below would like a lighter colour - yellow/gold/white banner background.

Banner sizes : 1600 x 700 and 1200x525
Square size for mobile : 960x960 and 640x640
Format: WebP and PNG

```html
<!DOCTYPE html>
<html lang="en">
<head>
<meta charset="utf-8">
<title>Ledgerwise Harbor – Young Starters Banner</title>
<link rel="stylesheet" href="https://fonts.googleapis.com/css2?family=Poppins:wght@400;600;700&display=swap">
<style>
  :root {
    --page-bg: #ffffff;
    --banner-bg: #e9e9e9;
    --banner-bg-light: #f2f2f2;
    --navy: #161a45;
    --gold: #d8b35a;
    --peach: #f6dfbf;
    --photo-warm: 184, 97, 42;
    --photo-dark: 27, 29, 34;
  }
  * { margin: 0; padding: 0; box-sizing: border-box; }
  html, body {
    width: 1200px;
    height: 1001px;
    overflow: hidden;
    background: var(--page-bg);
  }
  .banner {
    position: absolute;
    left: 0;
    top: 238px;
    width: 1200px;
    height: 525px;
    overflow: hidden;
    background: linear-gradient(120deg, var(--banner-bg) 0%, var(--banner-bg-light) 45%, var(--banner-bg) 100%);
    font-family: "Poppins", sans-serif;
    color: var(--navy);
  }
  .banner__art {
    position: absolute;
    left: 0;
    top: 0;
  }
  .banner__hero {
    position: absolute;
    left: 640px;
    top: 10px;
    width: 560px;
    height: 515px;
    background:
      radial-gradient(ellipse 34% 40% at 84% 74%, rgba(var(--photo-dark), 0.85) 0%, rgba(var(--photo-dark), 0.55) 55%, rgba(var(--photo-dark), 0) 100%),
      radial-gradient(ellipse 42% 62% at 46% 58%, rgba(var(--photo-warm), 0.95) 0%, rgba(var(--photo-warm), 0.7) 55%, rgba(var(--photo-warm), 0) 100%);
  }
  .banner__copy {
    position: absolute;
    left: 85px;
    top: 68px;
    width: 480px;
  }
  .banner__headline {
    font-weight: 700;
    font-size: 50px;
    line-height: 54px;
    letter-spacing: -0.3px;
  }
  .banner__sub {
    margin-top: 22px;
    font-weight: 400;
    font-size: 21.5px;
    line-height: 29px;
  }
  .banner__cta {
    position: absolute;
    left: 80px;
    top: 377px;
    width: 172px;
    height: 58px;
    border-radius: 29px;
    background: var(--gold);
    color: var(--navy);
    font-weight: 700;
    font-size: 22px;
    line-height: 58px;
    text-align: center;
    text-decoration: none;
  }
  .banner__dots {
    position: absolute;
    left: 320px;
    top: 360px;
  }
</style>
</head>
<body>
  <section class="banner">
    <svg class="banner__art" width="1200" height="525" viewBox="0 0 1200 525" aria-hidden="true">
      <defs>
        <linearGradient id="peach-fade" x1="0" y1="0" x2="1" y2="0">
          <stop offset="0" stop-color="var(--peach)" stop-opacity="0"/>
          <stop offset="0.35" stop-color="var(--peach)" stop-opacity="0.7"/>
          <stop offset="1" stop-color="var(--peach)" stop-opacity="0.9"/>
        </linearGradient>
      </defs>
      <rect x="880" y="0" width="320" height="525" fill="url(#peach-fade)"/>
      <circle cx="853" cy="360" r="243" fill="var(--gold)"/>
      <rect x="1060" y="12" width="65" height="65" fill="var(--gold)"/>
      <rect x="998" y="74" width="65" height="65" fill="var(--gold)"/>
    </svg>

    <div class="banner__hero" role="img" aria-label="Photo: smiling young man in an orange shirt using his phone, beside a laptop showing an investing dashboard"></div>

    <div class="banner__copy">
      <h1 class="banner__headline">Start smart.<br>Invest with<br>confidence.</h1>
      <p class="banner__sub">Learn the basics, set your first goal,<br>and build a long-term plan with<br>Ledgerwise Harbor.</p>
    </div>

    <a class="banner__cta" href="#">Start Free</a>

    <svg class="banner__dots" width="220" height="90" viewBox="0 0 220 90" aria-hidden="true">
      <g fill="var(--navy)">
        <circle cx="10" cy="10" r="4.5"/><circle cx="49" cy="10" r="4.5"/><circle cx="88" cy="10" r="4.5"/>
        <circle cx="127" cy="10" r="4.5"/><circle cx="166" cy="10" r="4.5"/><circle cx="205" cy="10" r="4.5"/>
        <circle cx="10" cy="78" r="4.5"/><circle cx="49" cy="78" r="4.5"/><circle cx="88" cy="78" r="4.5"/>
        <circle cx="127" cy="78" r="4.5"/><circle cx="166" cy="78" r="4.5"/><circle cx="205" cy="78" r="4.5"/>
      </g>
    </svg>
  </section>
</body>
</html>
```